Dental Practice based in Melbourne needs header designed for mobile website

Verdant Dental Carlow needs logo modified (better color scheme)and the header needs good use of colors (Green should be one of them) . The overall scheme is attached below. Please maintain the overall position of the logo in the center just like the way it is. Icons that should be present : Verdant Dental Carlow, Phone number with phone icon, Menu bar, Book now, search icon, Logo. in the center.

```html
<!DOCTYPE html>
<html lang="en">
<head>
<meta charset="UTF-8">
<title>Verdant Dental Carlow — Mobile Header</title>
<link rel="stylesheet" href="https://fonts.googleapis.com/css2?family=Questrial&display=swap">
<style>
  :root {
    --green: #1a7322;
    --green-soft: #6aa86f;
    --white: #ffffff;
    --ink: #000000;
    --field: #e8e8e8;
    --photo-light: #e9ecef;
    --photo-blue: #2f6fc0;
    --photo-skin: #d9b39b;
  }
  * { margin: 0; padding: 0; box-sizing: border-box; }
  html, body { width: 675px; height: 1200px; overflow: hidden; background: var(--white); }
  body { position: relative; font-family: "Questrial", "Century Gothic", sans-serif; }

  .top-band { position: absolute; left: 0; top: 0; width: 675px; height: 117px; background: var(--green); }
  .top-rule { position: absolute; left: 0; top: 134px; width: 675px; height: 9px; background: var(--green); }

  .brand-badge {
    position: absolute; left: 262px; top: 45px; width: 151px; height: 151px;
    border-radius: 50%; background: var(--white);
    display: flex; align-items: center; justify-content: center;
  }
  .brand-badge__disc {
    width: 112px; height: 112px; border-radius: 50%; background: var(--green);
    display: flex; align-items: center; justify-content: center; text-align: center;
    color: var(--white); font-size: 17px; line-height: 1.15;
  }

  .menu-toggle { position: absolute; left: 24px; top: 192px; width: 67px; height: 48px; }
  .menu-toggle span {
    position: absolute; left: 0; width: 67px; height: 9px; border-radius: 5px; background: var(--ink);
  }
  .menu-toggle span:nth-child(1) { top: 0; }
  .menu-toggle span:nth-child(2) { top: 19px; }
  .menu-toggle span:nth-child(3) { top: 38px; }

  .search-field {
    position: absolute; left: 124px; top: 193px; width: 427px; height: 46px;
    border-radius: 7px; background: var(--field);
  }
  .search-field svg { position: absolute; right: 20px; top: 10px; }

  .call-button {
    position: absolute; left: 599px; top: 193px; width: 51px; height: 51px;
    border: 3px solid var(--green); border-radius: 6px;
    display: flex; align-items: center; justify-content: center;
  }

  .wordmark {
    position: absolute; left: 0; top: 270px; width: 675px; height: 40px;
    display: flex; justify-content: center; align-items: center;
    font-size: 30px; color: var(--ink);
  }
  .wordmark__part { padding: 0 17px; }
  .wordmark__part--accent { color: var(--green); }
  .wordmark__divider { width: 1.5px; height: 26px; background: var(--green); }

  .hero {
    position: absolute; left: 0; top: 342px; width: 675px; height: 329px;
    background: linear-gradient(90deg, var(--photo-blue) 0%, var(--photo-light) 28%, var(--photo-skin) 48%, var(--photo-light) 70%, #b9bec6 100%);
  }
  .hero-dots { position: absolute; left: 313px; top: 651px; display: flex; gap: 9px; }
  .hero-dots span { width: 11px; height: 11px; border-radius: 50%; background: var(--green-soft); }
  .hero-dots span.is-active { background: var(--green); }
</style>
</head>
<body>
  <header class="site-header">
    <div class="top-band"></div>
    <div class="top-rule"></div>

    <div class="brand-badge">
      <div class="brand-badge__disc">Verdant<br>Dental</div>
    </div>

    <div class="menu-toggle" aria-label="Menu"><span></span><span></span><span></span></div>

    <div class="search-field" aria-label="Search">
      <svg width="27" height="27" viewBox="0 0 27 27" fill="none" stroke="#000" stroke-width="3" stroke-linecap="round">
        <circle cx="11" cy="11" r="8.5"/>
        <line x1="17.5" y1="17.5" x2="24.5" y2="24.5"/>
      </svg>
    </div>

    <div class="call-button" aria-label="Call">
      <svg width="28" height="28" viewBox="0 0 24 24">
        <path fill="#1a7322" d="M6.6 10.8a15.1 15.1 0 0 0 6.6 6.6l2.2-2.2c.3-.3.7-.4 1-.2 1.1.4 2.3.6 3.6.6.6 0 1 .4 1 1V20c0 .6-.4 1-1 1C10.6 21 3 13.4 3 4c0-.6.4-1 1-1h3.5c.6 0 1 .4 1 1 0 1.3.2 2.5.6 3.6.1.3 0 .7-.2 1z"/>
      </svg>
    </div>

    <div class="wordmark">
      <span class="wordmark__part">Verdant</span>
      <span class="wordmark__divider"></span>
      <span class="wordmark__part wordmark__part--accent">Dental</span>
      <span class="wordmark__divider"></span>
      <span class="wordmark__part">Carlow</span>
    </div>
  </header>

  <section class="hero" role="img" aria-label="Smiling patient in a blue dental chair with a dentist holding instruments"></section>
  <div class="hero-dots"><span></span><span class="is-active"></span><span></span></div>
</body>
</html>
```